The Maplecrest School Facebook

The Maplecrest School is a day care center and educational service provider, and we are based in Brandon, Florida. We would like to see designs that follow the pattern of our webpage regarding style, colors, and logo. The web page is not up yet, but we attached a screenshot for your reference.
Updates
Project Deadline Extended
Reason: So far the submitted designs fall below my expectations. I know you guys can do better! I up loaded nice quality pictures I purchased today... Hope this and the other materials helps to inspire you. Good luck!
Industry/Entity Type
It Service
Look and feel
Each slider illustrates characteristics of the customer's brand and the style your logo design should communicate.

```html
<!DOCTYPE html>
<html lang="en">
<head>
<meta charset="UTF-8">
<title>The Maplecrest School – Facebook Cover</title>
<link href="https://fonts.googleapis.com/css2?family=Montserrat:wght@600&display=swap" rel="stylesheet">
<style>
  :root {
    --page-bg: #ffffff;
    --navy: #061a33;
    --navy-ring: #0c2a4d;
    --navy-laurel: #0b2746;
    --star-blue: #17426b;
    --gold: #fbbf0f;
    --white: #ffffff;
    --photo-light: #f3e3d2;
    --photo-warm: #d9a77e;
    --photo-bright: #e98a6a;
    --photo-cool: #7fb0d8;
  }
  html, body {
    margin: 0;
    padding: 0;
    width: 1200px;
    height: 1000px;
    overflow: hidden;
    background: var(--page-bg);
  }
  .canvas {
    position: relative;
    width: 1200px;
    height: 1000px;
  }
  .cover {
    position: absolute;
    left: 285px;
    top: 383px;
    width: 630px;
    height: 233px;
    background: var(--navy);
    overflow: hidden;
  }
  .cover-art {
    position: absolute;
    inset: 0;
    width: 630px;
    height: 233px;
  }
  .school-name {
    font-family: 'Montserrat', sans-serif;
    font-weight: 600;
    fill: var(--white);
    font-size: 11px;
    letter-spacing: 0.5px;
    text-transform: uppercase;
  }
</style>
</head>
<body>
<div class="canvas">
  <section class="cover" aria-label="The Maplecrest School cover banner">
    <svg class="cover-art" viewBox="0 0 630 233" xmlns="http://www.w3.org/2000/svg">
      <defs>
        <path id="star" d="M0,-1 L0.235,-0.324 L0.951,-0.309 L0.380,0.124 L0.588,0.809 L0,0.4 L-0.588,0.809 L-0.380,0.124 L-0.951,-0.309 L-0.235,-0.324Z"/>
        <linearGradient id="children-tones" x1="0" y1="0" x2="1" y2="1">
          <stop offset="0%" stop-color="var(--photo-cool)"/>
          <stop offset="30%" stop-color="var(--photo-bright)"/>
          <stop offset="55%" stop-color="var(--photo-warm)"/>
          <stop offset="80%" stop-color="var(--photo-light)"/>
          <stop offset="100%" stop-color="var(--photo-warm)"/>
        </linearGradient>
      </defs>

      <g class="background-rings" fill="none" stroke="var(--navy-ring)" stroke-width="5">
        <circle cx="315" cy="116" r="300"/>
        <circle cx="315" cy="116" r="316"/>
        <circle cx="315" cy="116" r="212"/>
      </g>

      <circle class="laurel-band" cx="315" cy="116" r="178" fill="none"
              stroke="var(--navy-laurel)" stroke-width="40"
              role="img" aria-label="Faint laurel wreath decoration around the central ring"/>

      <g class="side-stars" fill="var(--star-blue)">
        <use href="#star" transform="translate(62 76) scale(11)"/>
        <use href="#star" transform="translate(55 124) scale(20)"/>
        <use href="#star" transform="translate(71 167) scale(11)"/>
        <use href="#star" transform="translate(567 76) scale(11)"/>
        <use href="#star" transform="translate(575 124) scale(20)"/>
        <use href="#star" transform="translate(558 167) scale(11)"/>
      </g>

      <circle class="gold-ring" cx="315" cy="116" r="152" fill="var(--gold)"/>
      <circle class="inner-field" cx="315" cy="116" r="137" fill="var(--white)"/>

      <circle class="children-photo" cx="315" cy="116" r="84" fill="none"
              stroke="url(#children-tones)" stroke-width="56" opacity="0.85"
              role="img" aria-label="Photo of smiling children standing in a circle, seen from above"/>

      <circle class="school-seal" cx="315" cy="116" r="52" fill="var(--navy)"/>
      <text class="school-name" x="315" y="106" text-anchor="middle">The</text>
      <text class="school-name" x="315" y="121" text-anchor="middle">Maplecrest</text>
      <text class="school-name" x="315" y="136" text-anchor="middle">School</text>
    </svg>
  </section>
</div>
</body>
</html>
```